Website Header with Logo Design for Plumbing Business

We require a website banner (including a logo) for use on a customer website.  The company name is Brookvale Plumbing & Heating Services, and they are mainly involved with general plumbing and heating in response to emergency call outs, scheduled repairs and maintenance (rather than kitchens and bathroom installations which are a relatively small part of the overall business).

The design of the banner should include a logo for the company which can be used elsewhere on stationery and other promotional material.

The details that would needed to be included on the banner are as follows:

• Brookvale Plumbing & Heating Services

• 020 7946 0382 – Call Us 24/7

• An appropriate image and a logo (may be a text only logo).

The old / draft banner is attached - it must be an improvement on this.

Industry/Entity Type

Business

Logo Text

Brookvale Plumbing & Heating Services

Requirements
Must have
• Size: 850 w x 250 h
• Web ready JPG web banner with logo - no borders, or designer annotations
• Vector file (EPS/AI) of the logo

```html
<!DOCTYPE html>
<html lang="en">
<head>
<meta charset="utf-8">
<title>Brookvale Plumbing &amp; Heating Services – Web Banner</title>
<link rel="stylesheet" href="https://fonts.googleapis.com/css2?family=Montserrat:wght@800&family=Open+Sans:wght@400&display=swap">
<style>
  :root {
    --navy: #111b27;
    --white: #ffffff;
    --yellow: #ffd21f;
    --rim-red: #d9231c;
    --rim-orange: #f2780f;
    --rim-yellow: #ffd21f;
    --mark-blue: #1f86e0;
    --mark-blue-deep: #0d4f9e;
    --chrome-light: #f4f7fa;
    --chrome-mid: #b9c7d4;
    --chrome-dark: #6f8397;
    --water-blue: #9fc1de;
    --basin-white: #eef2f6;
    --flame-dark: #03060b;
    --flame-blue: #2f6cff;
    --flame-cyan: #6fb0ff;
  }
  html, body {
    margin: 0;
    padding: 0;
    overflow: hidden;
    background: var(--white);
  }
  .banner {
    position: relative;
    width: 1200px;
    height: 352px;
    overflow: hidden;
    background: var(--white);
  }
  .photo {
    position: absolute;
    top: 0;
    height: 352px;
  }
  .photo--tap {
    left: 0;
    width: 460px;
    background:
      radial-gradient(ellipse 260px 90px at 150px 330px, var(--basin-white) 0%, rgba(238,242,246,0.6) 55%, transparent 80%),
      radial-gradient(ellipse 60px 200px at 300px 250px, rgba(255,255,255,0.85) 0%, rgba(159,193,222,0.5) 50%, transparent 85%),
      radial-gradient(ellipse 170px 150px at 170px 90px, var(--chrome-light) 0%, var(--chrome-mid) 45%, transparent 80%),
      radial-gradient(ellipse 120px 160px at 80px 210px, var(--chrome-dark) 0%, rgba(111,131,151,0.4) 50%, transparent 85%),
      linear-gradient(100deg, var(--chrome-mid) 0%, var(--chrome-light) 40%, var(--water-blue) 75%, var(--chrome-light) 100%);
  }
  .photo--flame {
    right: 0;
    width: 460px;
    background:
      radial-gradient(ellipse 200px 60px at 330px 120px, rgba(111,176,255,0.9) 0%, rgba(47,108,255,0.55) 40%, transparent 75%),
      radial-gradient(ellipse 70px 150px at 250px 230px, rgba(47,108,255,0.85) 0%, rgba(47,108,255,0.3) 50%, transparent 85%),
      radial-gradient(ellipse 140px 120px at 380px 300px, rgba(47,108,255,0.6) 0%, rgba(20,50,140,0.3) 50%, transparent 85%),
      radial-gradient(ellipse 170px 60px at 400px 190px, #000 0%, transparent 80%),
      var(--flame-dark);
  }
  .panel {
    position: absolute;
    left: 0;
    top: 0;
    width: 1200px;
    height: 352px;
  }
  .brand {
    position: absolute;
    left: 444px;
    top: 44px;
    display: flex;
    align-items: center;
    gap: 18px;
  }
  .brand__dot {
    width: 88px;
    height: 88px;
    border-radius: 50%;
    background: radial-gradient(circle at 40% 35%, var(--mark-blue) 0%, var(--mark-blue-deep) 100%);
    flex: none;
  }
  .brand__name {
    margin: 0;
    font-family: "Montserrat", sans-serif;
    font-weight: 800;
    font-size: 31px;
    line-height: 34px;
    letter-spacing: -0.5px;
    color: var(--white);
    text-transform: uppercase;
  }
  .divider {
    position: absolute;
    left: 352px;
    top: 204px;
    width: 496px;
    height: 3px;
    background: var(--white);
  }
  .phone {
    position: absolute;
    left: 0;
    width: 1206px;
    top: 216px;
    margin: 0;
    text-align: center;
    font-family: "Montserrat", sans-serif;
    font-weight: 800;
    font-size: 53px;
    line-height: 66px;
    color: var(--yellow);
  }
  .availability {
    position: absolute;
    left: 0;
    width: 1216px;
    top: 278px;
    margin: 0;
    text-align: center;
    font-family: "Open Sans", sans-serif;
    font-weight: 400;
    font-size: 50px;
    line-height: 60px;
    letter-spacing: -1px;
    color: var(--white);
  }
</style>
</head>
<body>
  <header class="banner">
    <div class="photo photo--tap" role="img" aria-label="Photo of a chrome mixer tap running water into a white basin"></div>
    <div class="photo photo--flame" role="img" aria-label="Photo of blue gas flames on a burner against a dark background"></div>

    <svg class="panel" viewBox="0 0 1200 352" aria-hidden="true">
      <defs>
        <linearGradient id="rim" x1="0" y1="0" x2="0" y2="1">
          <stop offset="0" stop-color="var(--rim-red)"/>
          <stop offset="0.45" stop-color="var(--rim-orange)"/>
          <stop offset="1" stop-color="var(--rim-yellow)"/>
        </linearGradient>
      </defs>
      <ellipse cx="600" cy="176" rx="268" ry="340" fill="url(#rim)"/>
      <ellipse cx="600" cy="176" rx="246" ry="326" fill="var(--navy)"/>
    </svg>

    <div class="brand">
      <span class="brand__dot"></span>
      <h1 class="brand__name">Brookvale<br>Plumbing<br>&amp; Heating<br>Services</h1>
    </div>

    <div class="divider"></div>
    <p class="phone">020 7946 0382</p>
    <p class="availability">Call Us 24/7</p>
  </header>
</body>
</html>
```